Figure for Manufacture of Wound Healing Gel

Who we are: We are a nationally funded bioengineering laboratory at Harlow Ridge University conducting research on the tendon healing properties of a gel manufactured from real tendon.

What we need: We require a figure piece that will be included in an academic publication. With that in mind, the figure must be professional, clear, and concise. A reader would need to glance at the figure for only a moment to understand the process of how we manufacture and store tendon gel. Actual pictures of the in-between steps are included and will need to be cropped to improve the professional look of the design.

The Details: The figure should stepwise show the process of how we manufacture and store tendon gel. In brief, we harvest tendon from donor cadavers. Those tendons undergo decellularization, lyophilization (fancy word for freeze-drying), and are milled into a fine powder. The powder is set in acidified water and treated with digestive enzymes. After 24 hrs, the gel is brought to physiologic pH and salinity and placed in vials. The vials are frozen and again lyophilized (this is so they can be stored and transported easily). Finally the samples are reconstituted with DI water.

The Figure: Should be a linear process (horizontal). The following are the actual steps we wish to include (steps need not be numbered necessarily as long as they are in logical order...

1.) A picture of harvested tendon (Step 1.jpg)
2.) Written description: "Decellularization, lyophilization, and milling"
3.) A picture of milled tendon powder (Step 2.jpg)
4.) Written description: "Digestion with pepsin before establishing physiologic pH and salinity".
5.) A picture of gel (Step 3.jpg)
6.) Written description: "Lyophilization of aliquots"
7.) A picture of freeze-dried gel (Step 4.jpg)
8.) Written description: "Reconstitution with DI water"
9.) A picture of reconstituted gel (Step 5.jpg)

Feel free to message for any questions, comments, or clarifications.

```html
<!DOCTYPE html>
<html lang="en">
<head>
<meta charset="utf-8">
<title>Manufacture and storage of Tendon Gel</title>
<link href="https://fonts.googleapis.com/css2?family=Carlito:wght@400;700&display=swap" rel="stylesheet">
<style>
  :root {
    --navy: #0a2150;
    --navy-text: #142a5c;
    --ink: #111111;
    --paper: #ffffff;
    --photo-dark: #2e2e2e;
    --photo-mid: #6b6864;
    --photo-light: #d9d4c8;
  }
  * { margin: 0; padding: 0; box-sizing: border-box; }
  html, body { width: 1200px; height: 1000px; overflow: hidden; background: var(--paper); }
  .figure {
    position: relative;
    width: 1200px;
    height: 1000px;
    font-family: "Carlito", "Calibri", sans-serif;
    color: var(--ink);
  }
  .figure-title {
    position: absolute; left: 77px; top: 39px;
    font-size: 21.5px; font-weight: 700; letter-spacing: -0.2px;
    white-space: nowrap;
  }
  .section-label {
    position: absolute;
    font-weight: 400; color: var(--navy-text);
    white-space: nowrap;
  }
  .section-label.manufacturing { left: 79px; top: 66px; font-size: 14.5px; }
  .section-label.storage { left: 721px; top: 45px; font-size: 15px; }
  .flow-shapes { position: absolute; left: 0; top: 0; }
  .step-label {
    position: absolute;
    width: 78px; height: 78px;
    display: flex; align-items: center; justify-content: center;
    text-align: center;
    font-size: 8.5px; line-height: 1.3;
    color: var(--ink);
    white-space: nowrap;
  }
  .step-photo { position: absolute; }
  .photo-dish {
    background: radial-gradient(ellipse at 50% 55%, var(--photo-light) 0%, var(--photo-mid) 40%, var(--photo-dark) 90%);
  }
  .photo-powder {
    background: radial-gradient(ellipse at 50% 50%, #f2eee4 0%, #b7b2a8 35%, #4a4846 85%);
  }
  .photo-gel {
    background: radial-gradient(ellipse at 50% 50%, #e8e8e8 0%, #8a8a8a 35%, #3a3a3a 85%);
  }
  .photo-vial {
    background: linear-gradient(90deg, #2c2c2c 0%, #3d3d3d 40%, #e7e3da 48%, #d6d2c6 52%, #3d3d3d 60%, #2c2c2c 100%);
  }
  .photo-vial-liquid {
    background: linear-gradient(90deg, #2c2c2c 0%, #3d3d3d 40%, #ece8d4 48%, #e0dcc4 52%, #3d3d3d 60%, #2c2c2c 100%);
  }
</style>
</head>
<body>
<div class="figure">
  <h1 class="figure-title">Manufacture and storage of Tendon Gel</h1>
  <div class="section-label manufacturing">Manufacturing process</div>
  <div class="section-label storage">Storage of Tendon Gel</div>

  <svg class="flow-shapes" width="1200" height="260" viewBox="0 0 1200 260" aria-hidden="true">
    <g fill="var(--navy)">
      <path d="M100,88 H258 C274,88 280,100 292,112 L300,138 L292,164 C280,176 274,190 258,190 H100 Z"/>
      <path d="M318,88 H474 C490,88 496,100 508,112 L516,138 L508,164 C496,176 490,190 474,190 H318 Z"/>
      <path d="M534,88 H690 C706,88 712,100 724,112 L732,138 L724,164 C712,176 706,190 690,190 H534 Z"/>
      <path d="M748,65 H912 C926,65 930,88 944,104 L950,138 L944,170 C930,186 930,225 912,225 H748 Z"/>
      <rect x="966" y="65" width="160" height="160"/>
    </g>
    <g fill="var(--paper)" stroke="var(--navy)" stroke-width="1">
      <circle cx="100" cy="138" r="39"/>
      <circle cx="318" cy="138" r="39"/>
      <circle cx="534" cy="138" r="39"/>
      <circle cx="748" cy="138" r="39"/>
      <circle cx="966" cy="138" r="39"/>
    </g>
  </svg>

  <div class="step-label" style="left:61px; top:99px;"><p>Harvesting of<br>Tendons from<br>cadaver sources</p></div>
  <div class="step-label" style="left:279px; top:99px;"><p>Decellularization,<br>lyophilization,<br>and milling</p></div>
  <div class="step-label" style="left:495px; top:99px;"><p>Digestion with<br>pepsin before<br>establishing<br>physiologic pH<br>and salinity</p></div>
  <div class="step-label" style="left:709px; top:99px;"><p>Lyophilization of<br>aliquots</p></div>
  <div class="step-label" style="left:927px; top:99px;"><p>Reconstitution<br>with DI water</p></div>

  <div class="step-photo photo-dish" role="img" aria-label="Photo of harvested tendons in a glass dish" style="left:153px; top:93px; width:99px; height:75px;"></div>
  <div class="step-photo photo-powder" role="img" aria-label="Photo of milled tendon powder in a glass dish" style="left:370px; top:93px; width:99px; height:75px;"></div>
  <div class="step-photo photo-gel" role="img" aria-label="Photo of digested tendon gel in a glass dish" style="left:585px; top:93px; width:99px; height:75px;"></div>
  <div class="step-photo photo-vial" role="img" aria-label="Photo of freeze-dried gel in a capped vial" style="left:796px; top:71px; width:103px; height:138px;"></div>
  <div class="step-photo photo-vial-liquid" role="img" aria-label="Photo of reconstituted gel in a capped vial" style="left:1013px; top:71px; width:105px; height:138px;"></div>
</div>
</body>
</html>
```